Quorvallen

I need a webiste built to sell digital downloads. I will be selling audio books. I will be selling them by the book and also by the chapter. I already have logos (attached) and some examples of covers. I'd like it simple. I was thinking a banner with a "featured" product which scrolls between three of four and a list of products below. Clicking on one of the covers will then go to a purchase page, which will include an option to but the entire title or chapter. I want something similar to the marlo VISTA website in theme and design. In terms of tabs, I will need ABOUT, TRUE CRIME, SPORT, MUSIC, AUTHORS.

```html
<!DOCTYPE html>
<html lang="en">
<head>
<meta charset="utf-8">
<title>Quorvallen — Audio Books</title>
<link href="https://fonts.googleapis.com/css2?family=Bebas+Neue&family=Montserrat:wght@400;500;600;700&display=swap" rel="stylesheet">
<style>
:root{
  --bg:#14151f;
  --bg-deep:#0f1019;
  --panel:#1b1c27;
  --green:#7cc242;
  --green-dark:#5e9a2e;
  --white:#ffffff;
  --muted:#c9ccd6;
  --row:#5a5b60;
  --row-dark:#3d3e43;
}
*{box-sizing:border-box;margin:0;padding:0}
html,body{width:1200px;height:3970px;overflow:hidden}
body{background:var(--bg);color:var(--white);font-family:"Montserrat",sans-serif;position:relative}
.head{font-family:"Bebas Neue",sans-serif;font-weight:400;letter-spacing:.5px;line-height:1}
.abs{position:absolute}

/* hero */
.hero{position:absolute;left:0;top:0;width:1200px;height:634px;background:linear-gradient(90deg,#121a33 0%,#16203a 45%,#1b2235 100%);overflow:hidden}
.hero-art{position:absolute;left:640px;top:0;width:560px;height:634px;background:linear-gradient(90deg,rgba(22,32,58,1) 0%,#3a3f4a 35%,#6d6f73 70%,#9a9a98 100%)}
.brand{position:absolute;left:108px;top:70px;font-family:"Bebas Neue",sans-serif;font-size:34px;color:var(--green);display:flex;align-items:center;gap:8px}
.brand .dot{width:14px;height:14px;border-radius:50%;background:var(--green)}
.nav{position:absolute;top:62px;left:408px;display:flex;gap:48px;font-size:15px;font-weight:500;color:var(--white)}
.btn-green{background:var(--green);color:var(--white);font-family:"Bebas Neue",sans-serif;font-size:18px;display:flex;align-items:center;justify-content:center;border-radius:2px}
.signup{position:absolute;left:997px;top:52px;width:92px;height:34px}
.hero h1{position:absolute;left:110px;top:208px;font-size:116px;line-height:.98;font-family:"Bebas Neue",sans-serif;font-weight:400}
.play{position:absolute;left:112px;top:451px;width:174px;height:43px;gap:10px}
.play svg{width:12px;height:12px}
.start{position:absolute;left:300px;top:451px;width:144px;height:43px;border:1.5px solid var(--white);display:flex;align-items:center;justify-content:center;font-family:"Bebas Neue",sans-serif;font-size:18px;border-radius:2px}

/* featured */
.section-title{font-family:"Bebas Neue",sans-serif;font-size:40px}
.featured-title{left:110px;top:725px}
.view-all{left:1010px;top:742px;color:var(--green);font-size:17px;font-weight:500}
.carousel{position:absolute;left:111px;top:813px;display:flex;gap:9px}
.cover{width:131px;height:190px}
.arrow-left{left:62px;top:890px;width:14px;height:14px}

/* latest */
.latest{position:absolute;left:0;top:1109px;width:1200px;height:835px;background:radial-gradient(circle at 50% 50%,#1f1f24 0%,#19191d 70%,#141418 100%)}
.latest-title{left:0;width:1200px;text-align:center;top:1180px}
.cover-frame{left:112px;top:1272px;width:281px;height:271px;border:5px solid var(--green)}
.disc{left:356px;top:1313px;width:200px;height:200px;border-radius:50%;background:radial-gradient(circle,#14151f 0 14px,#f1f1f1 15px 40px,#e2e2e2 41px 100%)}
.cover-book{left:147px;top:1305px;width:281px;height:273px;background:linear-gradient(120deg,#9a9a9a 0%,#d8d8d8 40%,#c2272d 60%,#e9e9e9 100%)}
.book-title{left:111px;top:1614px;font-size:28px}
.book-text{left:111px;top:1664px;width:300px;font-size:15px;line-height:30px;color:var(--muted)}
.learn{left:110px;top:1802px;width:160px;height:47px;border-radius:24px;background:var(--green);font-size:15px;font-weight:700;display:flex;align-items:center;justify-content:center}

.player{left:588px;top:1275px;width:501px;height:581px;background:#2a2b30;border-radius:4px;overflow:hidden}
.player-top{position:absolute;left:0;top:0;width:501px;height:134px;background:#18181c}
.thumb{position:absolute;left:16px;top:14px;width:112px;height:106px;background:linear-gradient(120deg,#8a8a8a,#d9d9d9 50%,#b72a2e)}
.thumb-play{position:absolute;left:48px;top:46px;width:38px;height:38px;border-radius:50%;background:#e9e9e9}
.track-name{position:absolute;left:138px;top:16px;font-size:15px;font-weight:700;line-height:26px}
.controls{position:absolute;left:138px;top:80px;display:flex;gap:20px;align-items:center}
.controls svg{width:14px;height:14px;fill:#fff}
.seek{width:118px;height:4px;background:#666;border-radius:2px}
.time{position:absolute;right:14px;top:108px;font-size:13px}
.progress{position:absolute;left:0;top:134px;width:501px;height:9px;background:#45464b}
.progress i{display:block;width:135px;height:100%;background:var(--green)}
.rows{position:absolute;left:0;top:145px;width:490px}
.row{height:43.7px;display:flex;justify-content:space-between;align-items:center;padding:0 22px;font-size:14px;border-bottom:1px solid #77787c;background:var(--row)}
.row.now{background:var(--row-dark)}
.scroll{position:absolute;right:0;top:145px;width:11px;height:436px;background:#fff}
.scroll i{display:block;margin-top:40px;height:36px;background:var(--green)}

/* offline */
.offline-circle{left:203px;top:2053px;width:424px;height:424px;border-radius:50%;background:var(--green)}
.offline-screen{left:109px;top:2100px;width:466px;height:327px;border:6px solid #fff;background:linear-gradient(135deg,#6b4a33,#b98a5e 50%,#3d2d22)}
.offline-phone{left:486px;top:2208px;width:114px;height:226px;border:6px solid #f1f1f1;border-radius:16px;background:linear-gradient(180deg,#2c2e36,#15161c)}
.offline-phone span{position:absolute;left:0;right:0;top:96px;text-align:center;font-family:"Bebas Neue",sans-serif;font-size:16px;color:var(--green)}
.offline-title{left:640px;top:2075px;font-size:42px;line-height:54px}
.offline-text{left:642px;top:2180px;width:455px;font-size:15px;line-height:30px;color:var(--muted)}
.subscribe-btn{left:643px;top:2338px;width:122px;height:43px}

/* faq */
.faq-title{left:0;width:1200px;text-align:center;top:2604px}
.faq{left:212px;width:804px;height:70px;border-radius:35px;background:var(--panel);display:flex;align-items:center;padding-left:8px}
.faq .num{width:56px;height:56px;border-radius:50%;background:#3b3c46;display:flex;align-items:center;justify-content:center;font-family:"Bebas Neue",sans-serif;font-size:26px}
.faq .q{margin-left:26px;font-family:"Bebas Neue",sans-serif;font-size:22px;flex:1}
.faq .sign{width:60px;font-size:24px;color:#6e707a}
.faq.open{background:var(--green)}
.faq.open .num{background:transparent}
.faq.open .q{margin-left:2px}
.faq.open .sign{color:#fff}
.answer{left:308px;top:3110px;width:660px;border-left:2px solid var(--green);padding-left:16px;font-size:14px;line-height:26px;color:var(--muted)}
.answer p+p{margin-top:25px}

/* newsletter */
.news{left:111px;top:3354px;width:978px;height:234px;background:var(--panel);border-radius:18px}
.news-title{left:143px;top:3408px;font-size:40px}
.news-text{left:144px;top:3464px;width:440px;font-size:14px;line-height:24px;color:var(--muted)}
.email{left:641px;top:3414px;width:415px;height:54px;border:1.5px solid #d9dbe3;display:flex;align-items:center;padding-left:30px;font-size:14px}
.news-btn{left:642px;top:3486px;width:140px;height:52px}

/* footer */
.footer{position:absolute;left:0;top:3600px;width:1200px;height:370px;background:linear-gradient(180deg,#151724 0%,#0f1522 100%)}
.foot-brand{left:112px;top:3694px;font-family:"Bebas Neue",sans-serif;font-size:50px;color:var(--green)}
.foot-text{left:111px;top:3770px;width:640px;font-size:14px;line-height:26px;color:var(--muted)}
.connect{left:897px;top:3690px;font-family:"Bebas Neue",sans-serif;font-size:17px}
.social{top:3733px;width:34px;height:34px}
.copy{left:111px;top:3898px;font-size:14px;color:var(--muted)}
</style>
</head>
<body>

<header class="hero">
  <div class="hero-art" role="img" aria-label="Featured audio book cover: prison corridor with barred gate and the author's name"></div>
  <div class="brand"><span class="dot"></span>Quorvallen</div>
  <nav class="nav"><span>About</span><span>True Crime</span><span>Sport</span><span>Music</span><span>Authors</span></nav>
  <div class="btn-green signup">Sign Up</div>
  <h1>Welcome to<br>Quorvallen</h1>
  <div class="btn-green play"><svg viewBox="0 0 10 10"><path d="M1 0l9 5-9 5z" fill="#fff"/></svg>Play Audio Book</div>
  <div class="start">Get Started</div>
</header>

<h2 class="abs section-title featured-title">Featured Products</h2>
<span class="abs view-all">View All</span>
<svg class="abs arrow-left" viewBox="0 0 14 14"><path d="M9 2L4 7l5 5" stroke="#fff" stroke-width="2" fill="none"/></svg>
<div class="carousel">
  <div class="cover" role="img" aria-label="Prison book cover" style="background:linear-gradient(180deg,#d7d7d7,#3a3a3a)"></div>
  <div class="cover" role="img" aria-label="Pink eye poster" style="background:radial-gradient(circle,#2fb4c6 0 12%,#f6c8d6 30%,#fdf0f4)"></div>
  <div class="cover" role="img" aria-label="Colourful band illustration poster" style="background:linear-gradient(135deg,#1b1d3c,#e85a8a 50%,#f2b53a)"></div>
  <div class="cover" role="img" aria-label="Jazz saxophone poster" style="background:linear-gradient(180deg,#f2efe6,#d7362f 55%,#1a1a1a)"></div>
  <div class="cover" role="img" aria-label="Vintage concert ticket poster" style="background:linear-gradient(180deg,#e8e2d2,#b9b1a0)"></div>
  <div class="cover" role="img" aria-label="Red festival poster with dove" style="background:linear-gradient(180deg,#d9262c,#b21d22)"></div>
  <div class="cover" role="img" aria-label="Charity concert globe poster" style="background:linear-gradient(180deg,#2b5fb8,#f3d34a 60%,#e7e2d6)"></div>
  <div class="cover" role="img" aria-label="Yellow singer concert poster" style="background:linear-gradient(180deg,#f1c44a,#e0a52b)"></div>
</div>

<section class="latest" role="img" aria-label="Background of scattered vinyl records"></section>
<h2 class="abs section-title latest-title">Latest Audio Book</h2>
<div class="abs cover-frame"></div>
<div class="abs disc"></div>
<div class="abs cover-book" role="img" aria-label="Audio book cover with author portrait and red title lettering"></div>
<h3 class="abs head book-title">The Last Street Crew Final</h3>
<p class="abs book-text">Lorem ipsum dolor sit amet, consectetur adipiscing elit, sed do eiusmod tempor incididunt ut labore et dolore magna aliqua. Quis ipsum</p>
<div class="abs learn">LEARN MORE</div>

<div class="abs player">
  <div class="player-top">
    <div class="thumb" role="img" aria-label="Audio book cover thumbnail"></div>
    <div class="thumb-play"><svg viewBox="0 0 38 38" width="38" height="38"><path d="M15 12l12 7-12 7z" fill="#7cc242"/></svg></div>
    <div class="track-name">THE LAST STREET CREW<br>FINAL</div>
    <div class="controls">
      <svg viewBox="0 0 10 10"><path d="M10 0v10L2 5z"/></svg>
      <svg viewBox="0 0 10 10"><path d="M1 0l9 5-9 5z"/></svg>
      <svg viewBox="0 0 12 10"><path d="M0 3h3l4-3v10L3 7H0z"/><path d="M9 2q2 3 0 6" stroke="#fff" fill="none"/></svg>
      <div class="seek"></div>
    </div>
    <div class="time">1:40 &nbsp;/ 4:16</div>
  </div>
  <div class="progress"><i></i></div>
  <div class="rows">
    <div class="row now"><span>Lorem ipsum</span><span>4:16</span></div>
    <div class="row"><span>Lorem ipsum</span><span>4:16</span></div>
    <div class="row"><span>Lorem ipsum</span><span>4:16</span></div>
    <div class="row"><span>Lorem ipsum</span><span>4:16</span></div>
    <div class="row"><span>Lorem ipsum</span><span>4:16</span></div>
    <div class="row"><span>Lorem ipsum</span><span>4:16</span></div>
    <div class="row"><span>Lorem ipsum</span><span>4:16</span></div>
    <div class="row"><span>Lorem ipsum</span><span>4:16</span></div>
    <div class="row"><span>Lorem ipsum</span><span>4:16</span></div>
    <div class="row"><span>Lorem ipsum</span><span>4:16</span></div>
  </div>
  <div class="scroll"><i></i></div>
</div>

<div class="abs offline-circle"></div>
<div class="abs offline-screen" role="img" aria-label="Person holding a tablet browsing audio book titles"></div>
<div class="abs offline-phone"><span>Quorvallen</span></div>
<h2 class="abs head offline-title">Download your shows to<br>watch offline.</h2>
<p class="abs offline-text">Lorem ipsum dolor sit amet, consectetur adipiscing elit, sed do eiusmod tempor incididunt ut labore et dolore magna aliqua. Quis ipsum suspendisse ultrices gravida. Risus commodo viverra maecenas accumsan lacus vel facilisis.</p>
<div class="abs btn-green subscribe-btn">Subscribe</div>

<h2 class="abs section-title faq-title">Frequently Asked Questions</h2>
<div class="abs faq" style="top:2744px"><div class="num">01</div><div class="q">Lorem ipsum dolor sit amet, consectetur adipiscing elit</div><div class="sign">+</div></div>
<div class="abs faq" style="top:2848px"><div class="num">02</div><div class="q">Lorem ipsum dolor sit amet, consectetur adipiscing elit</div><div class="sign">+</div></div>
<div class="abs faq" style="top:2951px"><div class="num">03</div><div class="q">Lorem ipsum dolor sit amet, consectetur adipiscing elit</div><div class="sign">+</div></div>
<div class="abs faq open" style="top:3014px;left:211px;width:806px;height:73px"><div class="num">04</div><div class="q">Lorem ipsum dolor sit amet, consectetur adipiscing elit</div><div class="sign">–</div></div>
<div class="abs answer">
  <p>Lorem ipsum dolor sit amet, consectetur adipiscing elit, sed do eiusmod tempor incididunt ut labore et dolore magna aliqua. Quis ipsum suspendisse ultrices gravida. Risus commodo viverra maecenas accumsan lacus vel facilisis.</p>
  <p>Lorem ipsum dolor sit amet, consectetur adipiscing elit, sed do eiusmod tempor incididunt ut labore et dolore magna aliqua.</p>
</div>

<div class="abs news"></div>
<h2 class="abs section-title news-title">Subscribe to Newsletter</h2>
<p class="abs news-text">Lorem ipsum dolor sit amet, consectetur adipiscing elit, sed do eiusmod tempor</p>
<div class="abs email">Your Email Address</div>
<div class="abs btn-green news-btn">Subscribe</div>

<footer class="footer"></footer>
<div class="abs foot-brand">Quorvallen</div>
<p class="abs foot-text">Lorem ipsum dolor sit amet, consectetur adipiscing elit, sed do eiusmod tempor incididunt ut labore et dolore magna aliqua. Quis ipsum suspendisse ultrices gravida. Risus commodo viverra maecenas accumsan lacus vel facilisis.</p>
<div class="abs connect">Connect With Us</div>
<div class="abs social" style="left:898px;background:var(--green)"></div>
<div class="abs social" style="left:946px;background:#1d2030"></div>
<p class="abs copy">©Copyrights 2023 Quorvallen &nbsp;| &nbsp; All Rights Reserved</p>

</body>
</html>
```